Business Cards and others
Business cards, stationery, Powerpoint template and E-mail Header and Footer
Professional
Darian Lutrell
CEO
4827 Thornwick Ln
Harlow Glen OR 97344
darian@velmorix.com
www.velmorix.com

```html
<!DOCTYPE html>
<html lang="en">
<head>
<meta charset="utf-8">
<title>Velmorix Business Card</title>
<link rel="stylesheet" href="https://fonts.googleapis.com/css2?family=Ubuntu:wght@400;500;700&display=swap">
<style>
  :root {
    --stage: #2b2b2d;
    --card: #ffffff;
    --brand-blue: #2a9fdc;
    --band-light: #8fd0f2;
    --text-grey: #6f7478;
    --rule-grey: #d4d7da;
  }
  * { margin: 0; padding: 0; box-sizing: border-box; }
  html, body {
    width: 1200px; height: 780px; overflow: hidden;
    background: var(--stage);
    font-family: "Ubuntu", Arial, sans-serif;
  }
  .business-card {
    position: absolute; left: 100px; top: 104px;
    width: 1000px; height: 572px;
    background: var(--card);
    border-radius: 34px;
    overflow: hidden;
  }
  .name-band {
    position: absolute; left: 0; top: 48px; width: 100%; height: 112px;
    background: var(--brand-blue);
    border-bottom: 8px solid var(--band-light);
    color: #fff; text-align: center;
    display: flex; flex-direction: column; justify-content: center;
  }
  .person-name { font-size: 30px; font-weight: 700; letter-spacing: 0.3px; }
  .person-title { font-size: 20px; font-weight: 400; margin-top: 4px; }
  .brand-block {
    position: absolute; left: 90px; top: 250px; width: 420px;
    display: flex; flex-direction: column; align-items: center;
  }
  .brand-dot {
    width: 120px; height: 120px; border-radius: 50%;
    background: var(--brand-blue);
  }
  .brand-name {
    margin-top: 14px;
    font-size: 64px; font-weight: 500; color: var(--brand-blue);
    letter-spacing: -0.5px; line-height: 1;
  }
  .divider {
    position: absolute; left: 560px; top: 196px; width: 2px; height: 330px;
    background: var(--rule-grey);
  }
  .contact-column {
    position: absolute; left: 592px; top: 206px;
    color: var(--text-grey); font-size: 22px; line-height: 1.4;
  }
  .address { margin-bottom: 18px; }
  .contact-list { list-style: none; }
  .contact-list li {
    display: flex; align-items: center; gap: 14px; height: 38px;
  }
  .contact-list svg { width: 22px; height: 22px; flex: none; }
</style>
</head>
<body>
  <main class="business-card">
    <header class="name-band">
      <div class="person-name">Darian Lutrell</div>
      <div class="person-title">CEO</div>
    </header>

    <section class="brand-block">
      <div class="brand-dot"></div>
      <div class="brand-name">Velmorix</div>
    </section>

    <div class="divider"></div>

    <section class="contact-column">
      <p class="address">4827 Thornwick Ln<br>Harlow Glen OR 97344</p>
      <ul class="contact-list">
        <li>
          <svg viewBox="0 0 24 24"><path fill="#2a9fdc" d="M6.6 10.8a15 15 0 0 0 6.6 6.6l2.2-2.2c.3-.3.7-.4 1-.2 1.1.4 2.3.6 3.6.6.6 0 1 .4 1 1V20c0 .6-.4 1-1 1A17 17 0 0 1 3 4c0-.6.4-1 1-1h3.5c.6 0 1 .4 1 1 0 1.3.2 2.5.6 3.6.1.3 0 .7-.2 1z"/></svg>
          604-218-5570
        </li>
        <li>
          <svg viewBox="0 0 24 24"><path fill="#2a9fdc" d="M6.6 10.8a15 15 0 0 0 6.6 6.6l2.2-2.2c.3-.3.7-.4 1-.2 1.1.4 2.3.6 3.6.6.6 0 1 .4 1 1V20c0 .6-.4 1-1 1A17 17 0 0 1 3 4c0-.6.4-1 1-1h3.5c.6 0 1 .4 1 1 0 1.3.2 2.5.6 3.6.1.3 0 .7-.2 1z"/></svg>
          3127406615
        </li>
        <li>
          <svg viewBox="0 0 24 24"><rect x="6" y="2" width="12" height="20" rx="2" fill="#2a9fdc"/><rect x="8" y="5" width="8" height="11" fill="#fff"/><circle cx="12" cy="19" r="1.2" fill="#fff"/></svg>
          5038172294
        </li>
        <li>
          <svg viewBox="0 0 24 24"><rect x="2" y="5" width="20" height="14" rx="2" fill="#2a9fdc"/><path d="M3 6l9 7 9-7" fill="none" stroke="#fff" stroke-width="1.8"/></svg>
          darian@velmorix.com
        </li>
        <li>
          <svg viewBox="0 0 24 24"><circle cx="12" cy="12" r="10" fill="#2a9fdc"/><g fill="none" stroke="#fff" stroke-width="1.4"><ellipse cx="12" cy="12" rx="4" ry="10"/><path d="M2 12h20M4 7h16M4 17h16"/></g></svg>
          www.velmorix.com
        </li>
      </ul>
    </section>
  </main>
</body>
</html>
```